Design a BOLD Ad Design for Fitness Club

We are fitness facility that is about to run our new "Bright Parent Reboot" program and we need a bold design created for an ad that will run on Instagram and Facebook.

The ad needs to be eye catching, easy to read and attractive so that someone stops scrolling and clicks to join.

The add needs to be sized to 1080 x 1080, include our logo and the text "Bright Parent Reboot" and "Starting September 23rd"

I have included an example photo, which is to be used as an example only of a design style that stands out to us, (colors, female photo style, etc)

I have also included our logo, which the yellow color can be changed for this design.

Thank you and we look forward to seeing your design.

```html
<!DOCTYPE html>
<html lang="en">
<head>
<meta charset="utf-8">
<title>Bright Parent Reboot – Instagram Ad</title>
<link rel="stylesheet" href="https://fonts.googleapis.com/css2?family=Anton&family=Arimo:wght@400;700&family=Kaushan+Script&family=Oswald:wght@500;700&display=swap">
<style>
  :root {
    --ink: #000000;
    --paper: #ffffff;
    --magenta: #ff00ee;
    --magenta-soft: #f26ff0;
    --photo-warm: #5a3a2c;
    --photo-dark: #151515;
    --photo-blue: #1d3aa8;
  }
  * { margin: 0; padding: 0; box-sizing: border-box; }
  html, body { width: 1200px; height: 1200px; overflow: hidden; background: var(--ink); }
  .ad { position: relative; width: 1200px; height: 1200px; background: var(--ink); overflow: hidden; }

  .athlete-photo {
    position: absolute; left: 500px; top: 250px; width: 540px; height: 950px;
    border-radius: 260px 260px 0 0;
    background: radial-gradient(ellipse at 50% 18%, var(--photo-warm) 0%, #2b1e18 30%, var(--photo-dark) 55%, var(--photo-blue) 82%, #142a7a 100%);
    opacity: 0.9;
  }
  .weights-photo {
    position: absolute; left: 0; top: 900px; width: 520px; height: 300px;
    background: radial-gradient(ellipse at 55% 40%, #2a2622 0%, #0c0c0c 60%, transparent 80%);
  }

  .program-kicker {
    position: absolute; top: 72px; left: 0; width: 1200px;
    display: flex; justify-content: center; align-items: center; gap: 22px;
  }
  .program-kicker__text {
    font-family: "Arimo", Arial, sans-serif; font-weight: 400;
    font-size: 88px; line-height: 1; color: var(--magenta); letter-spacing: 1px;
  }
  .program-title {
    position: absolute; top: 150px; left: 0; width: 1200px; text-align: center;
    font-family: "Anton", Impact, sans-serif; font-size: 290px; line-height: 1;
    color: var(--paper); letter-spacing: 6px;
  }

  .accent-ring { position: absolute; }
  .accent-ring--pink { left: 905px; top: 490px; }
  .accent-ring--white { left: 62px; top: 1080px; }
  .dot-grid { position: absolute; }
  .dot-grid--white { left: 1030px; top: 448px; }
  .dot-grid--pink { left: 52px; top: 1058px; }

  .date-card { position: absolute; left: 111px; top: 472px; width: 478px; height: 506px; }
  .date-card__frame { position: absolute; inset: 0; }
  .date-card__starting {
    position: absolute; top: 30px; width: 100%; text-align: center;
    font-family: "Arimo", Arial, sans-serif; font-weight: 700; font-size: 82px;
    line-height: 1; color: var(--magenta);
  }
  .date-card__month {
    position: absolute; top: 118px; width: 100%; text-align: center;
    font-family: "Kaushan Script", cursive; font-size: 96px; line-height: 1.1;
    color: var(--paper); transform: rotate(-4deg);
  }
  .date-card__day {
    position: absolute; top: 240px; width: 100%; text-align: center;
    font-family: "Oswald", Arial, sans-serif; font-weight: 500; font-size: 222px;
    line-height: 1; color: transparent; -webkit-text-stroke: 4px var(--magenta);
    letter-spacing: 4px;
  }

  .brand { position: absolute; left: 111px; top: 918px; width: 478px; text-align: center; }
  .brand__name {
    font-family: "Anton", Impact, sans-serif; font-size: 68px; line-height: 1;
    color: var(--paper); letter-spacing: 1px;
  }
  .brand__tagline {
    margin-top: 6px; font-family: "Arimo", Arial, sans-serif; font-weight: 700;
    font-size: 11px; letter-spacing: 2px; color: var(--magenta);
  }

  .web-address {
    position: absolute; left: 1122px; top: 1100px; transform-origin: left top;
    transform: rotate(-90deg); font-family: "Oswald", Arial, sans-serif;
    font-weight: 700; font-size: 40px; line-height: 1; color: var(--paper);
    letter-spacing: 1px; white-space: nowrap;
  }
  .web-address__accent { color: var(--magenta); }
</style>
</head>
<body>
<main class="ad">
  <div class="weights-photo" role="img" aria-label="Dimly lit weight plates and barbell on a gym floor"></div>
  <div class="athlete-photo" role="img" aria-label="Athletic woman in a black sports bra and blue leggings doing dumbbell curls"></div>

  <svg class="accent-ring accent-ring--pink" width="250" height="250" viewBox="0 0 250 250" aria-hidden="true">
    <circle cx="125" cy="125" r="98" fill="none" stroke="var(--magenta)" stroke-width="50"/>
  </svg>
  <svg class="dot-grid dot-grid--white" width="100" height="90" viewBox="0 0 100 90" aria-hidden="true">
    <g fill="var(--paper)">
      <circle cx="6" cy="6" r="5"/><circle cx="34" cy="6" r="5"/><circle cx="62" cy="6" r="5"/><circle cx="90" cy="6" r="5"/>
      <circle cx="6" cy="32" r="5"/><circle cx="34" cy="32" r="5"/><circle cx="62" cy="32" r="5"/><circle cx="90" cy="32" r="5"/>
      <circle cx="34" cy="58" r="5"/><circle cx="62" cy="58" r="5"/><circle cx="90" cy="58" r="5"/>
      <circle cx="62" cy="84" r="5"/><circle cx="90" cy="84" r="5"/>
    </g>
  </svg>
  <svg class="accent-ring accent-ring--white" width="200" height="200" viewBox="0 0 200 200" aria-hidden="true">
    <circle cx="100" cy="100" r="75" fill="none" stroke="var(--paper)" stroke-width="40"/>
  </svg>
  <svg class="dot-grid dot-grid--pink" width="100" height="90" viewBox="0 0 100 90" aria-hidden="true">
    <g fill="var(--magenta)">
      <circle cx="6" cy="6" r="5"/><circle cx="34" cy="6" r="5"/><circle cx="62" cy="6" r="5"/><circle cx="90" cy="6" r="5"/>
      <circle cx="6" cy="32" r="5"/><circle cx="34" cy="32" r="5"/><circle cx="62" cy="32" r="5"/><circle cx="90" cy="32" r="5"/>
      <circle cx="6" cy="58" r="5"/><circle cx="34" cy="58" r="5"/><circle cx="62" cy="58" r="5"/><circle cx="90" cy="58" r="5"/>
      <circle cx="34" cy="84" r="5"/><circle cx="62" cy="84" r="5"/>
    </g>
  </svg>

  <div class="program-kicker">
    <svg width="68" height="70" viewBox="0 0 68 70" aria-hidden="true">
      <g fill="var(--paper)"><rect x="0" y="25" width="8" height="20"/><rect x="14" y="12" width="14" height="46"/><rect x="34" y="0" width="14" height="70"/><rect x="54" y="30" width="14" height="10"/></g>
    </svg>
    <span class="program-kicker__text">BRIGHT PARENT</span>
    <svg width="68" height="70" viewBox="0 0 68 70" aria-hidden="true">
      <g fill="var(--paper)"><rect x="0" y="30" width="14" height="10"/><rect x="20" y="0" width="14" height="70"/><rect x="40" y="12" width="14" height="46"/><rect x="60" y="25" width="8" height="20"/></g>
    </svg>
  </div>
  <h1 class="program-title">REBOOT</h1>

  <section class="date-card">
    <svg class="date-card__frame" width="478" height="506" viewBox="0 0 478 506" aria-hidden="true">
      <defs>
        <linearGradient id="frameFade" x1="0" y1="0" x2="0" y2="1">
          <stop offset="0" stop-color="#ff00ee"/>
          <stop offset="0.7" stop-color="#f26ff0"/>
          <stop offset="1" stop-color="#ffffff"/>
        </linearGradient>
      </defs>
      <path d="M80 504 H42 A40 40 0 0 1 2 464 V42 A40 40 0 0 1 42 2 H436 A40 40 0 0 1 476 42 V464 A40 40 0 0 1 436 504 H400"
            fill="none" stroke="url(#frameFade)" stroke-width="3"/>
    </svg>
    <p class="date-card__starting">STARTING</p>
    <p class="date-card__month">September</p>
    <p class="date-card__day">23RD</p>
  </section>

  <div class="brand">
    <p class="brand__name">PulseForge</p>
    <p class="brand__tagline">PERSONAL GROUP TRAINING</p>
  </div>

  <p class="web-address">PULSE<span class="web-address__accent">FORGE</span>.COM</p>
</main>
</body>
</html>
```